Golf Brochure + Business Card Design Project – Larchmere Wellness.

Task Description

We are looking for a premium tri-fold brochure (8.5x11 letter, folded) plus a new business card design for Larchmere Wellness. Both need to look polished, elegant, and professional — something that would feel at home in a golf club environment.

Brochure Scope:
• Tri-fold brochure promoting our new golf-specific services
• Incorporate brand colors: deep hunter green, cream, and gold accents
• Clean, modern typography (professional, not playful)
• Layout will follow the copy provided (final copy attached, no rewriting needed)
• Imagery: mature golfers (50+), golf lifestyle shots, no generic stocky images
• Include QR code placement linking to booking page
• Deliverables: print-ready PDF with bleed/crop (CMYK), high-res PDF (digital), and source file (InDesign or Illustrator)

Business Card Scope:
• Front + back design
• Consistent with brand colors and fonts
• Space for name, title, phone, email, and website
• Deliverables: print-ready PDF with bleed/crop (CMYK) + source file (AI or InDesign)
• If possible, provide editable template for future staff cards

Timeline:
• First draft within 5–7 days
• 2 rounds of revisions included

Budget:
$300 USD (total for both brochure + business card)

I’ll provide finalized copy if you accept the project.
Project description (paste this whole block in that box)

We need a premium tri-fold brochure (8.5”×11” letter, folded) and a new business card design for Larchmere Wellness. This will be presented to golf course managers and members, so the look must be elegant, restrained, and country-club-classy.

Scope — Brochure
• Format: Tri-fold, 8.5”×11”. Please set 0.125” bleed on all sides and keep critical text ≥0.125–0.25” inside the trim.
• Purpose: Promote Larchmere Wellness’ golf-specific services for adults 50+.
• Copy: We will provide finalized copy in a Word doc after acceptance. No rewriting needed — please focus on layout and polish.
• Imagery (required):
• Golf-first images (ball on tee/green, mature golfers mid-swing, and golf course landscapes at golden hour).
• 1–2 real Larchmere Wellness gym photos on inside panels (trainer with client doing golf-relevant movement: stretch, rotation, balance).
• Visual style: Premium, quiet, lots of white/negative space, balanced grids; no clutter.
• Brand colors (required): Hunter Green #0C2E1F, Gold #CBA135, Cream #F5F2EB. Convert for CMYK print while preserving the look.
• Typography: Clean, legible serif + sans pairing (e.g., modern serif for headlines, humanist/neo-grotesk sans for body). You may propose suitable professional fonts; avoid playful/novelty fonts.
• Elements to include:
• Our logo (we will upload).
• QR code placement to booking page (we will supply the URL / QR asset).
• Simple icon treatment for the three complimentary options (Strength & Mobility, Stretch Therapy, Corelyn + Assessment).
• Deliverables:
• Print-ready PDF (CMYK, with bleed & crop marks, PDF/X-1a or PDF/X-4)
• High-res digital PDF (no bleed)
• Source file (InDesign or Illustrator) + packaged fonts/links or outlined type as appropriate.

Scope — Business Card
• Size: 3.5”×2” (US standard) with 0.125” bleed; keep text ≥0.125” from trim.
• Front/back design; consistent with brochure branding.
• Fields: Name, Title, Phone, Email, Website, Address; optional small QR on back.
• Deliverables: Print-ready PDF (CMYK, bleed & crops) + Source file (AI/INDD). Provide an editable template for staff names.

Process & Timing
• Initial concept for brochure + card within 5–7 days of acceptance.
• 2 rounds of revisions included.
• Please start with a clean layout concept using placeholder images/text blocks; we’ll drop in final copy/assets immediately after acceptance.

Stock & Licensing
• You may propose stock images that fit the brief (we’re fine approving Pictavault or equivalent). Please note any license fees separately if needed.

Usage Rights
• We require full usage rights to the final designs for print & digital.

Target Market(s)

Golfers 50+ in Victoria, BC: quality-oriented, health-conscious, want to play longer, stronger, and pain-free. Country-club aesthetic; expect polished, professional materials.

Industry/Entity Type

Health & Fitness — Golf Performance / Longevity Studio

Font styles to use
Serif
Sans Serif

Requirements
Must have
• • Golf-first imagery + 1–2 real Larchmere Wellness photos inside. • Brand colors: #0C2E1F (Hunter Green), #CBA135 (Gold), #F5F2EB (Cream). • Premium, restrained layout; ample negative space; no clutter. • Clean professional serif + sans type pairing; highly legible. • Space for logo and QR code (booking). • Correct print specs (bleed, crops, CMYK). • Deliverables: print-ready PDFs (brochure + card), digital PDF, source files.
Nice to have
• • Subtle texture or grain in backgrounds (very light) to add sophistication. • A second brochure cover variation (ball on tee vs. course landscape) at concept stage.
Should not have
• • Cheesy/posed “stocky” groups; overly young models; beer/alcohol imagery. • Over-saturated greens/blues; gimmicky gradients or clip art. • Generic fitness/bodybuilding shots unrelated to golf performance.

```html
<!DOCTYPE html>
<html lang="en">
<head>
<meta charset="utf-8">
<title>Larchmere Wellness – Business Card</title>
<link rel="stylesheet" href="https://fonts.googleapis.com/css2?family=Bebas+Neue&family=Inter:wght@400;600;700&display=swap">
<style>
  :root {
    --backdrop: #e6e7e9;
    --hunter: #2a4244;
    --gold: #c9a033;
    --cream: #f5f2eb;
    --ink: #2a4244;
  }
  * { margin: 0; padding: 0; box-sizing: border-box; }
  html, body {
    width: 1200px; height: 1200px; overflow: hidden;
    background: var(--backdrop);
  }
  .canvas {
    position: relative; width: 1200px; height: 1200px;
    background: var(--backdrop);
    font-family: "Inter", Arial, sans-serif;
  }
  .card {
    position: absolute; left: 269px; width: 662px; height: 378px;
  }
  .card--front { top: 183px; background: var(--hunter); }
  .card--back { top: 639px; background: var(--cream); }

  /* Front */
  .brand-mark {
    position: absolute; left: 50%; top: 74px; transform: translateX(-50%);
    width: 96px; height: 96px; border-radius: 50%;
    border: 3px solid var(--gold);
  }
  .brand-name {
    position: absolute; left: 0; right: 0; top: 196px;
    text-align: center; color: var(--gold);
    font-family: "Inter", Arial, sans-serif; font-weight: 600;
    font-size: 24px; letter-spacing: 0.04em; line-height: 1;
  }
  .tagline {
    position: absolute; left: 0; right: 0; top: 291px;
    text-align: center; color: var(--gold);
    font-family: "Bebas Neue", "Arial Narrow", sans-serif;
    font-size: 35px; line-height: 1; letter-spacing: 0.005em;
  }

  /* Back */
  .holder-name {
    position: absolute; left: 66px; top: 103px;
    color: var(--ink); font-weight: 700; font-size: 27px; line-height: 1;
  }
  .holder-title {
    position: absolute; left: 66px; top: 143px;
    color: var(--ink); font-weight: 400; font-size: 19px; line-height: 1;
    letter-spacing: 0.02em;
  }
  .holder-title .divider {
    display: inline-block; width: 1.5px; height: 24px; background: var(--ink);
    vertical-align: -5px; margin: 0 8px;
  }
  .contact-list { position: absolute; left: 66px; top: 198px; list-style: none; }
  .contact-item {
    display: flex; align-items: center; height: 26px;
    color: var(--ink); font-size: 20px; letter-spacing: 0.02em;
  }
  .contact-item svg {
    width: 21px; height: 21px; margin-right: 15px; flex: none;
    fill: none; stroke: var(--gold); stroke-width: 1.2;
    stroke-linejoin: round; stroke-linecap: round;
  }
</style>
</head>
<body>
<main class="canvas">
  <section class="card card--front" aria-label="Card front">
    <span class="brand-mark" aria-hidden="true"></span>
    <p class="brand-name">Larchmere Wellness</p>
    <p class="tagline">Strength • Mobility • Longevity</p>
  </section>

  <section class="card card--back" aria-label="Card back">
    <h1 class="holder-name">Claire-Anne Whitlow</h1>
    <p class="holder-title">Owner<span class="divider"></span>Larchmere Wellness</p>
    <ul class="contact-list">
      <li class="contact-item">
        <svg viewBox="0 0 24 24" aria-hidden="true"><path d="M6.5 2.5l3 4.5-2 2c1 2.6 3.6 5.3 6.5 6.5l2-2 4.5 3-1.8 3.2C12.5 21 3 11.5 3.3 4.3z"/></svg>
        250-555-0147
      </li>
      <li class="contact-item">
        <svg viewBox="0 0 24 24" aria-hidden="true"><rect x="2" y="5" width="20" height="14"/><path d="M2 5l10 8 10-8M2 19l7.5-7.5M22 19l-7.5-7.5"/></svg>
        claire-anne@larchmerewellness.biz
      </li>
      <li class="contact-item">
        <svg viewBox="0 0 24 24" aria-hidden="true"><circle cx="12" cy="12" r="9.5"/><ellipse cx="12" cy="12" rx="4.2" ry="9.5"/><path d="M2.5 12h19M4 7h16M4 17h16"/></svg>
        larchmerewellnessvictoria.com
      </li>
    </ul>
  </section>
</main>
</body>
</html>
```